Business cards - KESTO Roofing & Siding

We need simple business cards made up for our Roofing & Siding business based in Calgary Alberta.
The logo on one side of the card and potentially our slogan "Built to last, proven by seasons".
The other side could have:
-A small logo
-Rep name:
-Rep cell phone:
-Rep email:
-Office phone: 403-386-2049
-Website: PrairieShinglePros.com

We would like to incorporate the colours from our logo, especially the lite blue on the jpeg file. I have attached the ai file and jpeg file. We like the colours better on the jpeg file.

I do not require a money back guarantee

```html
<!DOCTYPE html>
<html lang="en">
<head>
<meta charset="utf-8">
<title>KESTO Roofing &amp; Siding – Business Cards</title>
<link rel="stylesheet" href="https://fonts.googleapis.com/css2?family=Montserrat:wght@500;600;700;800&family=Open+Sans:wght@400;600&display=swap">
<style>
  :root {
    --bg: #d9d9db;
    --card: #ffffff;
    --ink: #1e1e1e;
    --grey: #5a5a5c;
    --blue: #2f6fb7;
    --blue-lite: #4f88cc;
    --shadow: rgba(0,0,0,0.18);
  }
  * { margin: 0; padding: 0; box-sizing: border-box; }
  html, body { width: 1200px; height: 961px; overflow: hidden; background: var(--bg); }
  body { position: relative; font-family: "Open Sans", sans-serif; color: var(--ink); }

  .card {
    position: absolute;
    width: 560px; height: 320px;
    background: var(--card);
    border-radius: 26px;
    box-shadow: 0 10px 24px var(--shadow);
    overflow: hidden;
  }
  .card--front { left: 320px; top: 110px; }
  .card--back  { left: 320px; top: 520px; }

  .brand-name {
    font-family: "Montserrat", sans-serif; font-weight: 600;
    color: var(--grey); letter-spacing: 0.06em; text-transform: uppercase;
    white-space: nowrap;
  }

  /* front */
  .front-brand {
    position: absolute; left: 0; right: 0; top: 92px;
    display: flex; align-items: center; justify-content: center; gap: 14px;
  }
  .brand-mark { width: 30px; height: 30px; background: var(--blue-lite); flex: none; }
  .front-brand .brand-name { font-size: 30px; }
  .front-est {
    position: absolute; left: 0; right: 0; top: 148px; text-align: center;
    font-family: "Montserrat", sans-serif; font-weight: 500; font-size: 15px;
    letter-spacing: 0.18em; color: var(--grey);
  }
  .front-slogan {
    position: absolute; left: 0; right: 0; top: 226px; text-align: center;
    font-family: "Montserrat", sans-serif; font-weight: 800; font-size: 17px; color: var(--ink);
  }

  /* back */
  .back-brand { position: absolute; left: 40px; top: 40px; }
  .back-brand .brand-name { font-size: 22px; }
  .rep-name {
    position: absolute; left: 40px; top: 104px;
    font-family: "Montserrat", sans-serif; font-weight: 800; font-size: 26px;
    color: var(--blue); text-transform: uppercase; white-space: nowrap;
  }
  .rep-title { position: absolute; left: 40px; top: 142px; font-size: 16px; color: var(--ink); }
  .contact-list { position: absolute; left: 40px; top: 184px; list-style: none; }
  .contact-list li {
    display: flex; align-items: center; gap: 12px;
    font-size: 16px; line-height: 32px; color: var(--ink); white-space: nowrap;
  }
  .contact-list svg { width: 16px; height: 16px; flex: none; }

  .back-accent { position: absolute; right: 48px; top: 110px; text-align: center; }
  .back-accent .accent-square { width: 70px; height: 70px; background: var(--blue-lite); margin: 0 auto 16px; }
  .back-accent .est {
    font-family: "Montserrat", sans-serif; font-weight: 500; font-size: 22px;
    letter-spacing: 0.14em; color: var(--grey); white-space: nowrap;
  }
</style>
</head>
<body>

<section class="card card--front">
  <div class="front-brand">
    <span class="brand-mark"></span>
    <span class="brand-name">KESTO Roofing &amp; Siding</span>
  </div>
  <p class="front-est">Est. 1994</p>
  <p class="front-slogan">Built to last, proven by seasons</p>
</section>

<section class="card card--back">
  <div class="back-brand"><span class="brand-name">KESTO Roofing &amp; Siding</span></div>
  <h1 class="rep-name">Daniel Harper</h1>
  <p class="rep-title">Managing Director</p>
  <ul class="contact-list">
    <li>
      <svg viewBox="0 0 24 24" aria-hidden="true"><path fill="#2f6fb7" d="M6.6 10.8a15.1 15.1 0 0 0 6.6 6.6l2.2-2.2a1 1 0 0 1 1-.25 11.4 11.4 0 0 0 3.6.57 1 1 0 0 1 1 1V20a1 1 0 0 1-1 1A17 17 0 0 1 3 4a1 1 0 0 1 1-1h3.5a1 1 0 0 1 1 1c0 1.25.2 2.45.57 3.57a1 1 0 0 1-.25 1z"/></svg>
      403-386-2049
    </li>
    <li>
      <svg viewBox="0 0 24 24" aria-hidden="true"><path d="M2 5h20v14H2z M2 5l10 8 10-8" fill="none" stroke="#2f6fb7" stroke-width="2"/></svg>
      dharper@prairieshinglepros.com
    </li>
    <li>
      <svg viewBox="0 0 24 24" aria-hidden="true"><circle cx="12" cy="12" r="10" fill="none" stroke="#2f6fb7" stroke-width="2"/><path d="M2 12h20M12 2c3 3 3 17 0 20M12 2c-3 3-3 17 0 20" fill="none" stroke="#2f6fb7" stroke-width="1.6"/></svg>
      PrairieShinglePros.com
    </li>
  </ul>
  <div class="back-accent">
    <div class="accent-square"></div>
    <p class="est">Est. 1994</p>
  </div>
</section>

</body>
</html>
```